Create a "germ free" Poster Design Project

Hi we're a media business who sells advertising space on a unique dispensing device that also sanitizes your hands.

I'm looking for a poster design that highlights the need to sanitize hands which removes 99.9% of germs and also promotes a healthy & clean lifestyle.
(you may want to use kid friendly images of bugs to highlight germs)
Whilst the primary message will be to sanitize your hands the secondary message is also to "use this space" to advertise on.

The poster should be colorful yet simple and not too wordy.

Thanks

Target Market(s)

General cunsumer public but more specifically women and moms

Industry/Entity Type

Advertising

Requirements
Must have
• A central picture (animated or real) to highlight the practice of sanitizing hands (or removing germs)
Perhaps an arrow down to invite consumers to "try it now, its free'
Nice to have
• Referal to our web site: Brelvona.com.au (currently not operational) and email info@brelvona.com.au
Perhaps an image of a baby's hand with a creative tag line.
Should not have
• Nothing too gross looking

```html
<!DOCTYPE html>
<html lang="en">
<head>
<meta charset="utf-8">
<title>Germs Don't Like Me – Poster</title>
<link rel="stylesheet" href="https://fonts.googleapis.com/css2?family=Open+Sans:wght@600&family=Michroma&family=Arimo:wght@400&display=swap">
<style>
  :root {
    --frame-blue: #2f5fe0;
    --sky-light: #d4ecfa;
    --sky-mid: #a9dbf6;
    --paper: #ffffff;
    --headline-green: #1f9a3a;
    --ink: #0b0b14;
    --arrow-blue: #1f6fe6;
    --drop-blue: #5aaef0;
    --drop-pale: #cfe9fb;
    --skin: #f6c690;
    --skin-light: #fbe0c0;
  }
  html, body {
    margin: 0;
    padding: 0;
    overflow: hidden;
  }
  .poster {
    position: relative;
    width: 982px;
    height: 1200px;
    box-sizing: border-box;
    border: 6px solid var(--frame-blue);
    overflow: hidden;
    background:
      linear-gradient(160deg, transparent 0 40%, var(--sky-light) 40% 48%, transparent 60%),
      linear-gradient(200deg, var(--sky-mid) 0 8%, var(--paper) 22% 70%, var(--sky-light) 85%, var(--sky-mid) 100%);
  }
  .headline {
    position: absolute;
    top: 44px;
    left: 0;
    width: 100%;
    margin: 0;
    text-align: center;
    font-family: "Open Sans", sans-serif;
    font-weight: 600;
    font-size: 88px;
    line-height: 1.2;
    letter-spacing: -2px;
    color: var(--headline-green);
  }
  .subline {
    position: absolute;
    top: 160px;
    left: 208px;
    margin: 0;
    font-family: "Michroma", sans-serif;
    font-weight: 700;
    font-size: 62px;
    line-height: 1.2;
    letter-spacing: 2px;
    color: var(--ink);
    white-space: pre;
  }
  .hero-illustration {
    position: absolute;
    left: 270px;
    top: 272px;
    width: 450px;
    height: 478px;
    box-sizing: border-box;
    border: 3px dashed var(--drop-blue);
    border-radius: 28px;
    background: linear-gradient(180deg, var(--skin-light) 0%, var(--drop-pale) 35%, var(--drop-blue) 60%, var(--skin) 100%);
  }
  .cta {
    position: absolute;
    top: 772px;
    left: 393px;
    margin: 0;
    font-family: "Arimo", sans-serif;
    font-size: 100px;
    line-height: 1.1;
    color: var(--ink);
  }
  .down-arrow {
    position: absolute;
    left: 481px;
    top: 885px;
    width: 124px;
    height: 222px;
  }
  .website {
    position: absolute;
    top: 1104px;
    left: 0;
    width: 100%;
    margin: 0;
    text-align: center;
    font-family: "Arimo", sans-serif;
    font-size: 72px;
    line-height: 1;
    color: var(--ink);
  }
</style>
</head>
<body>
  <main class="poster">
    <h1 class="headline">Germs Don’t like me!</h1>
    <p class="subline">But  You Will :)</p>
    <div class="hero-illustration" role="img" aria-label="Illustration area: cartoon cupped hands rubbing a blue sanitiser droplet, with bubbles and coloured germ specks being washed away"></div>
    <p class="cta">Try Me</p>
    <svg class="down-arrow" viewBox="0 0 124 222" aria-hidden="true">
      <g fill="var(--arrow-blue)">
        <rect x="28" y="0" width="68" height="8"/>
        <rect x="28" y="22" width="68" height="8"/>
        <rect x="28" y="44" width="68" height="8"/>
        <rect x="28" y="66" width="68" height="8"/>
        <rect x="34" y="86" width="56" height="30"/>
        <polygon points="0,112 124,112 62,222"/>
      </g>
    </svg>
    <p class="website">Brelvona.com.au</p>
  </main>
</body>
</html>
```